Kitchen and bathroom exhaust fan cleaning business card design

A new business cleaning domestic - not commercial - exhaust/extractor fans in kitchens, bathrooms and en suites and kitchen range hood filters.

We would like a bright colour suggesting cleanliness (such a syellow or light green?)

I would like to see on the card preferably on the reverse:

"We clean kitchen and bathroom exhaust fans & Vormo Heatlites
and
clean and repair range hood filters and replace carbon filters

We give Pensioner discounts

Designers pls note the TM in the contact filed after Brisko Airworks should be superscript as in the trademark sign. On the reverse of the card, I would like:: "We clean kitchen and bathroom exhaust fans & Vormo Heatlites & clean and repair range hood filters and replace carbon filters We give Pensioner discounts

Reason: I will be out of the country for several days

Target Market(s)

people who are too lazy or too busy to clean their fan units and pensioners and others who are unable to do it.

Industry/Entity Type

Business

Contact Information for Business Card

Brisko AirworksTM Designer pls note the TM should be superscript as in the trademark sign
Alan Petworth
Mob: 0491 570 263
Email: briskoairworks@postlume.net
PO Box 7152, Hawker ACT 2614

Requirements
Must have
• Designer pls note the TM in the contact filed after Brisko Airworks should be superscript as in the trademark sign.

On the reverse

and

```html
<!DOCTYPE html>
<html lang="en">
<head>
<meta charset="utf-8">
<title>Brisko Airworks – Business Card</title>
<link href="https://fonts.googleapis.com/css2?family=Jura:wght@500;600&family=Noto+Serif:wght@400&display=swap" rel="stylesheet">
<style>
  :root {
    --page-bg: #e6e6e4;
    --card-top: #ffffff;
    --card-bottom: #e9e9e9;
    --ink: #2b2b2b;
    --ink-soft: #3c3c3c;
    --band: #353535;
    --accent: #1aa9e4;
  }
  html, body {
    margin: 0;
    width: 1200px;
    height: 892px;
    overflow: hidden;
    background: var(--page-bg);
  }
  .canvas {
    position: relative;
    width: 1200px;
    height: 892px;
  }
  .card {
    position: absolute;
    left: 250px;
    width: 700px;
    height: 400px;
    background: linear-gradient(160deg, var(--card-top) 30%, var(--card-bottom) 100%);
    box-shadow: 0 12px 28px rgba(0,0,0,0.2);
    overflow: hidden;
  }
  .card--front { top: 30px; }
  .card--back { top: 462px; }
  .card__band {
    position: absolute;
    inset: 0;
    width: 100%;
    height: 100%;
  }
  .contact-block {
    position: absolute;
    left: 48px;
    top: 58px;
    font-family: "Jura", sans-serif;
    color: var(--ink);
  }
  .person__name {
    margin: 0;
    font-size: 21px;
    font-weight: 600;
    letter-spacing: 1px;
    text-transform: uppercase;
  }
  .person__role {
    margin: 2px 0 0;
    font-size: 14px;
    font-weight: 500;
    letter-spacing: 1px;
    text-transform: uppercase;
  }
  .address {
    margin: 32px 0 0;
    font-size: 15px;
    font-weight: 600;
    line-height: 1.25;
    font-style: normal;
  }
  .contact-list {
    list-style: none;
    margin: 26px 0 0;
    padding: 0;
    font-size: 13.5px;
    font-weight: 600;
    color: var(--ink-soft);
  }
  .contact-list li {
    display: flex;
    align-items: center;
    gap: 10px;
    height: 24px;
  }
  .contact-list svg {
    width: 13px;
    height: 13px;
    fill: var(--ink-soft);
  }
  .brand {
    position: absolute;
    left: 385px;
    top: 118px;
    margin: 0;
    font-family: "Noto Serif", serif;
    font-weight: 400;
    font-size: 48px;
    line-height: 1.08;
    color: var(--accent);
  }
  .brand sup {
    font-size: 16px;
    vertical-align: super;
    line-height: 0;
    margin-left: 2px;
  }
  .services {
    position: absolute;
    left: 190px;
    top: 110px;
    width: 440px;
    margin: 0;
    font-family: "Jura", sans-serif;
    color: var(--ink);
  }
  .services__text {
    margin: 0;
    font-size: 19px;
    font-weight: 600;
    line-height: 1.4;
  }
  .services__offer {
    margin: 28px 0 0;
    font-size: 21px;
    font-weight: 600;
    color: var(--accent);
  }
</style>
</head>
<body>
<div class="canvas">
  <section class="card card--front">
    <svg class="card__band" viewBox="0 0 700 400" aria-hidden="true">
      <polygon points="294,400 329,332 381,332 346,400" fill="var(--band)"/>
    </svg>

    <div class="contact-block">
      <p class="person__name">Alan Petworth</p>
      <p class="person__role">General Manager</p>
      <address class="address">PO Box 7152,<br>Hawker ACT 2614</address>
      <ul class="contact-list">
        <li>
          <svg viewBox="0 0 24 24"><path d="M6.6 10.8a15 15 0 0 0 6.6 6.6l2.2-2.2a1 1 0 0 1 1-.25 11 11 0 0 0 3.6.6 1 1 0 0 1 1 1V20a1 1 0 0 1-1 1A17 17 0 0 1 3 4a1 1 0 0 1 1-1h3.5a1 1 0 0 1 1 1 11 11 0 0 0 .6 3.6 1 1 0 0 1-.25 1z"/></svg>
          0491 570 263
        </li>
        <li>
          <svg viewBox="0 0 24 24"><path d="M7 2h10a2 2 0 0 1 2 2v16a2 2 0 0 1-2 2H7a2 2 0 0 1-2-2V4a2 2 0 0 1 2-2zm0 3v13h10V5z"/></svg>
          0491 570 264
        </li>
        <li>
          <svg viewBox="0 0 24 24"><path d="M7 2h9v5H7zM4 8h16a2 2 0 0 1 2 2v8h-4v4H6v-4H2v-8a2 2 0 0 1 2-2zm4 8v4h8v-4z"/></svg>
          0491 570 265
        </li>
        <li>
          <svg viewBox="0 0 24 24"><path d="M3 5h18a1 1 0 0 1 1 1v12a1 1 0 0 1-1 1H3a1 1 0 0 1-1-1V6a1 1 0 0 1 1-1zm1 2.2V17h16V7.2l-8 5.3z"/></svg>
          briskoairworks@postlume.net
        </li>
        <li>
          <svg viewBox="0 0 24 24"><path d="M12 2a10 10 0 1 0 0 20 10 10 0 0 0 0-20zm6.9 9h-3a15 15 0 0 0-1.3-5.6A8 8 0 0 1 18.9 11zM12 4.1c.9 1.3 1.8 3.6 1.9 6.9h-3.8c.1-3.3 1-5.6 1.9-6.9zM9.4 5.4A15 15 0 0 0 8.1 11h-3a8 8 0 0 1 4.3-5.6zM5.1 13h3a15 15 0 0 0 1.3 5.6A8 8 0 0 1 5.1 13zm6.9 6.9c-.9-1.3-1.8-3.6-1.9-6.9h3.8c-.1 3.3-1 5.6-1.9 6.9zm2.6-1.3a15 15 0 0 0 1.3-5.6h3a8 8 0 0 1-4.3 5.6z"/></svg>
          www.briskoairworks.net
        </li>
      </ul>
    </div>

    <p class="brand">Brisko<br>Airworks<sup>TM</sup></p>
  </section>

  <section class="card card--back">
    <svg class="card__band" viewBox="0 0 700 400" aria-hidden="true">
      <polygon points="70,0 128,0 86,84 28,84" fill="var(--band)"/>
    </svg>
    <div class="services">
      <p class="services__text">We clean kitchen and bathroom exhaust fans &amp; Vormo Heatlites &amp; clean and repair range hood filters and replace carbon filters</p>
      <p class="services__offer">We give Pensioner discounts</p>
    </div>
  </section>
</div>
</body>
</html>
```